Banner Design Project

We are an Australian online lighting store based in Sydney.
Our website is "www.trelvamart.com.au"
We need someone you can create a 2 banners for our homepage.
We will have 3 banners rotating, the first banner will be our actual banner, the second one will be advertising Free Shipping Insurance and the third will advertising the 30 Day money back guaranty.
Don't be afraid to use words like Risk Free, 30 Day Money back Guaranty! etc....
The banner size:
599 x 186 px
The format should be given in .psd and .jpg
We need something slick and attractive that looks very promotional.
The banner should have the same look and feel as the website.
We are looking for someone long term, so if the job goes well, we might ask the person to design regularly for us in the future.

```html
<!DOCTYPE html>
<html lang="en">
<head>
<meta charset="utf-8">
<title>Free Shipping Insurance – Trelvamart</title>
<link href="https://fonts.googleapis.com/css2?family=Archivo+Black&family=Arimo:wght@400;700&display=swap" rel="stylesheet">
<style>
  :root {
    --bg-top: #f4f4f4;
    --bg-bottom: #d9d9d9;
    --headline-stroke: #f07a1e;
    --sea-deep: #1f3f5c;
    --sea-mid: #3f6a8a;
    --hull-orange: #e8632a;
    --deck-white: #e9eef2;
    --subline: #8c8c8c;
    --brand-text: #6a6a6a;
    --brand-dot: #f07a1e;
    --band-top: #3a72a8;
    --band-bottom: #1c4677;
    --band-edge: #6f9dcb;
  }
  html, body {
    margin: 0;
    padding: 0;
    overflow: hidden;
  }
  body {
    width: 1200px;
    height: 373px;
  }
  .banner {
    position: relative;
    width: 1200px;
    height: 373px;
    background: linear-gradient(180deg, var(--bg-top) 0%, var(--bg-bottom) 85%);
    overflow: hidden;
  }
  .banner__art {
    position: absolute;
    inset: 0;
    display: block;
  }
  .headline {
    font-family: 'Archivo Black', 'Arial Black', sans-serif;
  }
  .subline {
    font-family: 'Arimo', Arial, sans-serif;
    font-weight: 400;
    fill: var(--subline);
  }
  .brand {
    position: absolute;
    left: 870px;
    top: 222px;
    display: flex;
    align-items: center;
    gap: 12px;
  }
  .brand__dot {
    width: 34px;
    height: 34px;
    border-radius: 50%;
    background: var(--brand-dot);
  }
  .brand__name {
    font-family: 'Arimo', Arial, sans-serif;
    font-weight: 700;
    font-size: 50px;
    letter-spacing: -1px;
    color: var(--brand-text);
    line-height: 1;
  }
  .band {
    position: absolute;
    left: 0;
    right: 0;
    top: 316px;
    bottom: 0;
    background: linear-gradient(180deg, var(--band-top) 0%, var(--band-bottom) 100%);
    border-top: 2px solid var(--band-edge);
  }
</style>
</head>
<body>
  <div class="banner">
    <svg class="banner__art" width="1200" height="373" viewBox="0 0 1200 373">
      <defs>
        <linearGradient id="cargo-ship-tones" x1="0" y1="0" x2="1" y2="1">
          <stop offset="0" stop-color="var(--sea-mid)"/>
          <stop offset="0.35" stop-color="var(--hull-orange)"/>
          <stop offset="0.55" stop-color="var(--deck-white)"/>
          <stop offset="0.8" stop-color="var(--sea-mid)"/>
          <stop offset="1" stop-color="var(--sea-deep)"/>
        </linearGradient>
      </defs>
      <text class="headline" x="22" y="236" font-size="314"
            textLength="748" lengthAdjust="spacingAndGlyphs"
            fill="url(#cargo-ship-tones)" stroke="var(--headline-stroke)" stroke-width="4"
            role="img" aria-label="FREE, lettering filled with a photo of an orange and white cargo ship at sea">FREE</text>
      <text class="subline" x="22" y="292" font-size="60"
            textLength="748" lengthAdjust="spacing">SHIPPING INSURANCE</text>
    </svg>
    <div class="brand">
      <span class="brand__dot"></span>
      <span class="brand__name">Trelvamart</span>
    </div>
    <div class="band"></div>
  </div>
</body>
</html>
```